High-end residential home builder needs a business card design

We need a new business card design for a small residential construction company based in Boise, Idaho. We specialize in building custom high-end homes and remodels, with a focus on great design and craftsmanship.

We would like to use our current logo, but open to new color suggestions.
Just looking for a clean, sharp, modern design that looks high-end.

Target Market(s)

Upscale clientele

Industry/Entity Type

Contractor

Contact Information for Business Card

Company: Stonefield Custom Builders
Name: Marcus Tilley
Phone number: 208 367 4120
Email: MarcusTilleySCB@mailbox-example.com
Website: Stonefieldcustombuilders-example.com

Font styles to use
Serif
Sans Serif

Requirements
Must have
• Company Logo
Company name
My name
My phone number
My email
Company website
Nice to have
• I have attached a few photos of cards that I really like.

```html
<!DOCTYPE html>
<html lang="en">
<head>
<meta charset="utf-8">
<title>Stonefield Custom Builders – Business Card</title>
<link rel="stylesheet" href="https://fonts.googleapis.com/css2?family=Montserrat:wght@400;500&family=Open+Sans:wght@400&display=swap">
<style>
  :root {
    --backdrop: #3b3c39;
    --card: #161616;
    --card-edge: #0c0c0c;
    --pattern: #1d1d1d;
    --copper: #b8834e;
    --ink-light: #ecebe8;
    --ink-soft: #c9c8c4;
  }
  html, body {
    margin: 0;
    padding: 0;
    width: 1200px;
    height: 824px;
    overflow: hidden;
    background: var(--backdrop);
  }
  .canvas {
    position: relative;
    width: 1200px;
    height: 824px;
  }
  .card {
    position: absolute;
    top: 262px;
    width: 520px;
    height: 300px;
    background: var(--card);
    border: 1px solid var(--card-edge);
    box-sizing: border-box;
    overflow: hidden;
  }
  .card--front { left: 50px; }
  .card--back { left: 630px; }

  .front__pattern {
    position: absolute;
    inset: 0;
    background: var(--pattern);
    opacity: 0.55;
  }
  .front__brand {
    position: absolute;
    left: 82px;
    top: 108px;
    display: flex;
    align-items: center;
    gap: 22px;
  }
  .brand-square {
    width: 56px;
    height: 56px;
    border: 2px solid var(--copper);
    box-sizing: border-box;
  }
  .brand-name {
    font-family: "Montserrat", sans-serif;
    font-weight: 500;
    color: var(--copper);
    text-transform: uppercase;
    margin: 0;
  }
  .brand-name__main {
    display: block;
    font-size: 27px;
    letter-spacing: 6px;
    line-height: 1;
  }
  .brand-name__rule {
    display: block;
    height: 1px;
    background: var(--copper);
    margin: 9px 0 8px;
  }
  .brand-name__sub {
    display: block;
    font-size: 13px;
    letter-spacing: 5.4px;
    line-height: 1;
  }

  .back__brand {
    position: absolute;
    left: 48px;
    top: 106px;
    width: 140px;
    display: flex;
    flex-direction: column;
    align-items: center;
    gap: 14px;
  }
  .back__brand .brand-square { width: 48px; height: 48px; }
  .back__brand .brand-name {
    font-size: 10px;
    letter-spacing: 2.5px;
    text-align: center;
    line-height: 1.5;
  }
  .contact {
    position: absolute;
    left: 214px;
    top: 96px;
  }
  .contact__name {
    margin: 0 0 14px;
    font-family: "Montserrat", sans-serif;
    font-weight: 400;
    font-size: 22px;
    letter-spacing: 1.5px;
    color: var(--ink-light);
    text-transform: uppercase;
  }
  .contact__list {
    list-style: none;
    margin: 0;
    padding: 0;
    font-family: "Open Sans", sans-serif;
    font-size: 12.5px;
    color: var(--ink-soft);
  }
  .contact__item {
    display: flex;
    align-items: center;
    gap: 9px;
    margin-bottom: 7px;
  }
  .contact__icon {
    width: 12px;
    height: 12px;
    flex: none;
  }
</style>
</head>
<body>
<main class="canvas">
  <section class="card card--front" aria-label="Business card front">
    <div class="front__pattern" role="img" aria-label="Faint repeating brand pattern across the card"></div>
    <div class="front__brand">
      <div class="brand-square"></div>
      <h1 class="brand-name">
        <span class="brand-name__main">Stonefield</span>
        <span class="brand-name__rule"></span>
        <span class="brand-name__sub">Custom Builders</span>
      </h1>
    </div>
  </section>

  <section class="card card--back" aria-label="Business card back">
    <div class="back__brand">
      <div class="brand-square"></div>
      <p class="brand-name">Stonefield<br>Custom Builders</p>
    </div>
    <div class="contact">
      <h2 class="contact__name">Marcus Tilley</h2>
      <ul class="contact__list">
        <li class="contact__item">
          <svg class="contact__icon" viewBox="0 0 12 12" aria-hidden="true"><path d="M2.5 1 L4.5 1 L5.2 3.6 L4 4.6 Q5 7 7.4 8 L8.4 6.8 L11 7.5 L11 9.5 Q10.5 11 9 11 Q1 10 1 2.5 Q1 1 2.5 1 Z" fill="var(--copper)"/></svg>
          <span>208 367 4120</span>
        </li>
        <li class="contact__item">
          <svg class="contact__icon" viewBox="0 0 12 12" aria-hidden="true"><rect x="0.5" y="2" width="11" height="8" fill="var(--copper)"/><path d="M0.5 2 L6 6.5 L11.5 2" fill="none" stroke="var(--card)" stroke-width="1"/></svg>
          <span>MarcusTilleySCB@mailbox-example.com</span>
        </li>
        <li class="contact__item">
          <svg class="contact__icon" viewBox="0 0 12 12" aria-hidden="true"><circle cx="6" cy="6" r="5.5" fill="var(--copper)"/><g fill="none" stroke="var(--card)" stroke-width="0.8"><ellipse cx="6" cy="6" rx="2.4" ry="5.5"/><line x1="0.5" y1="6" x2="11.5" y2="6"/></g></svg>
          <span>Stonefieldcustombuilders-example.com</span>
        </li>
      </ul>
    </div>
  </section>
</main>
</body>
</html>
```